Viral food truck (ClipBuzz) needs menu

Our food truck has gone viral on ClipBuzz and we're now requesting a one-page food menu for a taco food truck, please use the logo attached as inspiration and stick to those colors when designing the menu. This is a bilingual menu, please ensure to make the English translation stand out as well.

Size: 8x12 landscape

LOGO - Morales's Taco Bar
318 W Orchard Ln (Entrada/Entrance Brightway Shopping Center)
Central Islip, NY 11548
Fri, 6 pm to 11:30 pm | Sat, 1 pm to 11:30 pm | Sun, 1 pm to 11:00 pm

Para horario y información / For pop-up, updated hours and information
Síganos/Follow Us: @moralestacobar

MENU

Tacos.....$4.75 ea
Selección de carne, cilantro, cebolla, salsa roja o verde
Choice of meat, cilantro, onion, red or green salsa

Selección de carne/Choice of Meat
Pollo (Chicken)
Carne Asada (Steak)
Al pastor (Marinated Pork)
Chorizo (Sausage)
Carnitas (Pulled Pork)
Mixta (steak & sausage)........$0.75 extra
Suadero (Brisket).......$0.75 extra
Lengua (Beef Tongue)......$0.75 extra
Tripa (Beef Tripe)......$0.75 extra

Antojitos/Appetizers
Tacos Dorados De Pollo.......$15.00
Taco Dorados De Carne.........$15.00
Quesadilla...........$10.00
Pollo (Chicken) | Carne Asada (Steak) | Queso (Cheese)
Pupusa Revueltas (Chicharone y Queso).........$3.50
Pupusa Queso............$3.50

Especiales / Specials
(#1) 4 Tacos..........$14
(#2) 4 Tacos Dorados/Flautas
Pollo, Creama, Queso Fresco, Aguacate
Chicken, Cream, Queso Fresco, Avocado
*(designer note: need a symbol here) (#3) Chicharones 1lb........$25.00

* Cantidad limitada y temoprada/Limited Quantity/Seasonal

BEBIDAS/BEVERAGES

Horchata.........$6.00

Agua Fresca.......$5.00
SABOR/FLAVOR
Limonada (Lemonade) | Jamaica (Hibiscus) | Sandia (Watermelon) | Piña (Pineapple) | Melon | Mango

Fizzo......$2.00
Zestle.....$2.00
Water.....$1.50
Bubblitos.......$3.00

Target Market(s)

Foodies

Industry/Entity Type

Food truck

Font styles to use
Sans Serif

Colors

Designer to choose colors to be used in the design.

Requirements
Must have
• Color and elements based on our logo, please also visit our Pictagram and Friendbook page for inspiration
Nice to have
• Vintage esthetic

```html
<!DOCTYPE html>
<html lang="en">
<head>
<meta charset="utf-8">
<title>Morales's Taco Bar – Menu</title>
<link rel="stylesheet" href="https://fonts.googleapis.com/css2?family=Anton&family=Catamaran:wght@500;600;700&display=swap">
<style>
  :root{
    --orange:#f26f1e;
    --ink:#1c1c1c;
    --charcoal:#2e2e2e;
    --light:#e9e7e4;
    --cream:#f3e3c3;
    --brown:#5a2b14;
    --white:#ffffff;
    --hours-ink:#3a2a28;
  }
  *{margin:0;padding:0;box-sizing:border-box}
  html,body{width:1200px;height:889px;overflow:hidden;background:var(--white)}
  body{font-family:"Catamaran",sans-serif;color:var(--white);position:relative}
  .sheet{position:absolute;left:52px;top:46px;width:1095px;height:796px;overflow:hidden;background:var(--ink)}
  .backdrop{position:absolute;left:0;top:0}
  .abs{position:absolute}

  .brand{position:absolute;width:124px;height:124px;border-radius:50%;background:var(--cream);
    display:flex;align-items:center;justify-content:center;text-align:center;
    font-weight:700;font-size:15px;line-height:1.1;color:var(--brown)}
  .brand-left{left:20px;top:10px}
  .brand-right{left:950px;top:10px}

  .photo{position:absolute;border-radius:50%}
  .photo-steak{left:139px;top:119px;width:296px;height:296px;background:radial-gradient(circle at 45% 50%,#7a4a30 0%,#c99d68 35%,#f5f3ef 62%)}
  .photo-tacos{left:667px;top:127px;width:284px;height:284px;background:radial-gradient(circle at 50% 50%,#b86a3c 0%,#e8d4b0 45%,#d9b68a 70%)}
  .photo-horchata{left:456px;top:207px;width:156px;height:172px;border-radius:10px 10px 18px 18px;background:linear-gradient(180deg,#f4f1ec,#e7ddd0)}

  .title{position:absolute;left:396px;top:35px;width:300px;text-align:center;font-family:"Anton",sans-serif;
    font-weight:400;font-size:132px;line-height:1;color:var(--white);transform:scaleX(.87);letter-spacing:2px}

  .hours{position:absolute;left:405px;top:379px;width:266px;height:82px}
  .hours svg{position:absolute;inset:0}
  .hours p{position:absolute;left:44px;font-weight:600;font-size:17px;line-height:1;color:var(--hours-ink);white-space:nowrap}

  .head{position:absolute;z-index:1;height:20px;font-weight:700;font-size:12.5px;line-height:20px;color:var(--white);white-space:nowrap}
  .head::before{content:"";position:absolute;left:-15px;right:-12px;top:1px;bottom:1px;background:var(--orange);border-radius:3px 9px 4px 10px;transform:skewX(-8deg);z-index:-1}

  .list{position:absolute;font-weight:500;font-size:11.4px;line-height:13.4px;color:var(--white)}
  .row{display:flex;align-items:baseline;white-space:nowrap}
  .row .dots{flex:1;border-bottom:1px dotted var(--white);margin:0 1px 3px}
  .head .row .dots{margin-bottom:5px}
  .note{font-size:8px;font-weight:500}

  .footer{position:absolute;left:0;top:741px;width:1095px;height:55px;background:var(--charcoal);border-top:2px solid var(--orange);text-align:center}
  .footer .addr{font-weight:500;font-size:11px;margin-top:7px}
  .footer .follow{font-weight:500;font-size:11px;color:var(--orange);margin-top:2px}
</style>
</head>
<body>
<main class="sheet">
  <svg class="backdrop" width="1095" height="796" viewBox="0 0 1095 796">
    <defs>
      <linearGradient id="foodTone" x1="0" y1="0" x2="1" y2="1">
        <stop offset="0" stop-color="#ecebea"/>
        <stop offset=".45" stop-color="#e6c9a0"/>
        <stop offset="1" stop-color="#ebe8e4"/>
      </linearGradient>
    </defs>
    <ellipse cx="548" cy="-453" rx="742" ry="955" fill="var(--orange)"/>
    <ellipse cx="548" cy="-453" rx="720" ry="934" fill="url(#foodTone)" role="img" aria-label="Photo of golden quesadillas with fresh herbs"/>
  </svg>

  <div class="brand brand-left">Morales's<br>Taco Bar</div>
  <div class="brand brand-right">Morales's<br>Taco Bar</div>

  <div class="photo photo-steak" role="img" aria-label="Plate of grilled steak with potato wedges and salad"></div>
  <div class="photo-horchata abs" role="img" aria-label="Glass of horchata with cinnamon stick"></div>
  <div class="photo photo-tacos" role="img" aria-label="Plate of tacos with pico de gallo and guacamole"></div>

  <h1 class="title">MENU</h1>

  <div class="hours">
    <svg width="266" height="82" viewBox="0 0 266 82"><path d="M8 14 L250 4 L262 20 L250 40 L258 62 L240 80 L20 78 L2 62 L12 44 L0 26 Z" fill="var(--orange)"/></svg>
    <p style="top:10px">FRI, 6 PM TO 11:30 PM</p>
    <p style="top:32px">SAT, 1 PM TO 11:30 PM</p>
    <p style="top:54px">SUN, 1 PM TO 11:00 PM</p>
  </div>

  <!-- Tacos -->
  <div class="head" style="left:46px;top:479px;width:252px">
    <div class="row"><span>TACOS</span><span class="dots"></span><span>$4.75 EA</span></div>
  </div>
  <div class="list" style="left:46px;top:505px">
    <div>Selección de carne, cilantro, cebolla, salsa roja o verde</div>
    <div>Choice of meat, cilantro, onion, red or green salsa</div>
  </div>

  <!-- Meat -->
  <div class="head" style="left:46px;top:560px;width:250px">SELECCIÓN DE CARNE/CHOICE OF MEAT</div>
  <div class="list" style="left:46px;top:580px;width:251px">
    <div class="row"><span>Pollo (Chicken)</span><span class="dots"></span><span>$0.00 extra</span></div>
    <div class="row"><span>Carne Asada (Steak)</span><span class="dots"></span><span>$0.00 extra</span></div>
    <div class="row"><span>Al pastor (Marinated Pork)</span><span class="dots"></span><span>$0.00 extra</span></div>
    <div class="row"><span>Chorizo (Sausage)</span><span class="dots"></span><span>$0.00 extra</span></div>
    <div class="row"><span>Carnitas (Pulled Pork)</span><span class="dots"></span><span>$0.00 extra</span></div>
    <div class="row"><span>Mixta (steak &amp; sausage)</span><span class="dots"></span><span>$0.75 extra</span></div>
    <div class="row"><span>Suadero (Brisket)</span><span class="dots"></span><span>$0.75 extra</span></div>
    <div class="row"><span>Lengua (Beef Tongue)</span><span class="dots"></span><span>$0.75 extra</span></div>
    <div class="row"><span>Tripa (Beef Tripe)</span><span class="dots"></span><span>$0.75 extra</span></div>
  </div>
  <div class="list note" style="left:44px;top:726px">* Cantidad limitada y temoprada/Limited Quantity/Seasonal</div>

  <!-- Appetizers -->
  <div class="head" style="left:327px;top:552px;width:160px">ANTOJITOS/APPETIZERS</div>
  <div class="list" style="left:327px;top:580px;width:252px">
    <div class="row"><span>Tacos Dorados De Pollo</span><span class="dots"></span><span>$15.00</span></div>
    <div class="row"><span>Taco Dorados De Carne</span><span class="dots"></span><span>$15.00</span></div>
    <div class="row"><span>Quesadilla</span><span class="dots"></span><span>$10.00</span></div>
    <div>Pollo (Chicken) | Carne Asada (Steak)</div>
    <div>Queso (Cheese) | Pupusa Revueltas</div>
    <div class="row"><span>(Chicharone y Queso)</span><span class="dots"></span><span>$3.50</span></div>
    <div class="row"><span>Pupusa Queso</span><span class="dots"></span><span>$3.50</span></div>
  </div>

  <!-- Specials -->
  <div class="head" style="left:608px;top:552px;width:162px">ESPECIALES / SPECIALS</div>
  <div class="list" style="left:608px;top:578px;width:251px">
    <div class="row"><span>(#1) 4 Tacos</span><span class="dots"></span><span>$14.00</span></div>
    <div>Selección de carne, cilantro, cebolla,</div>
    <div>salsa roja o verde</div>
    <div>Choice of meat, cilantro, onion,</div>
    <div>red or green salsa</div>
    <div class="row" style="margin-top:13px"><span>(#2) 4 Tacos Dorados/Flautas</span><span class="dots"></span><span>$0.00</span></div>
    <div>Pollo, Creama, Queso Fresco, Aguacate</div>
    <div>Chicken, Cream, Queso Fresco, Avocado</div>
    <div class="row" style="margin-top:13px;width:255px"><span>(#3) Chicharones 1lb</span><span class="dots"></span><span>$25.00</span></div>
  </div>

  <!-- Beverages -->
  <div class="head" style="left:895px;top:479px;width:150px">BEBIDAS/BEVERAGES</div>
  <div class="list" style="left:895px;top:506px;width:156px">
    <div class="row"><span>Horchata</span><span class="dots"></span><span>$6.00</span></div>
    <div class="row"><span>Agua Fresca</span><span class="dots"></span><span>$5.00</span></div>
  </div>

  <div class="head" style="left:895px;top:552px;width:124px">SABOR/FLAVOR</div>
  <div class="list" style="left:895px;top:578px;width:156px">
    <div>Limonada (Lemonade)</div>
    <div>Jamaica (Hibiscus)</div>
    <div>Sandia (Watermelon)</div>
    <div>Piña (Pineapple)</div>
    <div>Melon | Mango</div>
    <div class="row" style="margin-top:13px"><span>Fizzo</span><span class="dots"></span><span>$2.00</span></div>
    <div class="row"><span>Zestle</span><span class="dots"></span><span>$2.00</span></div>
    <div class="row"><span>Water</span><span class="dots"></span><span>$1.50</span></div>
    <div class="row"><span>Bubblitos</span><span class="dots"></span><span>$3.00</span></div>
  </div>

  <footer class="footer">
    <p class="addr">318 W Orchard Ln (Entrada/Entrance Brightway Shopping Center) Central Islip, NY 11548</p>
    <p class="follow">Para horario y información / For pop-up, updated hours and information Síganos/Follow Us: @moralestacobar</p>
  </footer>
</main>
</body>
</html>
```